VORELT B2B portal design
Fantastic design work, top communication and fast design changes! Many thanks,Jens & Uwe from VORELT
Zielgruppe
We are a B2B Cloud Services StartUp that creates B2B logistics & supply chain processes between customer and its suppliers.
Aufgabenstellung
We need a modern responsive able design, that should consider that we are NOT presenting goods or clothes or similar on the portal pages but we show mainly data grids, kpi dashboards, forms, and setting panels to our customer and their suppliers.
The design must be clean and straight not to distract people from the important information in these data grids, kpi dashboards, forms, and settings panels.
We need our logo perfectly embedded and the pages coloured around from grey to blue.
The Designer must be able to deliver a design and transfer it to a highly responsive HTML (5) template (without technical content or further functionality). This our programmers will implement afterwards in .Net.
We need in total 3 page templates:
1. Login Page
2. Main Page with overview over the following services text (each one shown in one tile)
"ZMS (Time Frame Management)"
"DMS (Document Management)"
"REMS (Reporting Management)"
-> Note: At the end we will have up to 12 or more tiles (services) so the design should be additive
3. Data grid (e.g. list of customers)/form (e.g. customer registration form) page to show some data grid with database data
See samples for each page enclosed!!

```html
<!DOCTYPE html>
<html lang="en">
<head>
<meta charset="utf-8">
<title>VORELT Portal – Grid Styling</title>
<link href="https://fonts.googleapis.com/css2?family=Ubuntu:wght@400;500;700&display=swap" rel="stylesheet">
<style>
:root{
  --navy:#0d2c48;
  --navy-hover:#163a58;
  --flyout:#0f2e4a;
  --panel:#e1e6ea;
  --page:#f7f8f9;
  --line:#cfd6dc;
  --text:#3d4650;
  --muted:#66707a;
  --head:#e3e7eb;
  --stripe:#eaf5fa;
  --white:#ffffff;
  --pager-active:#b9bec3;
}
*{box-sizing:border-box;margin:0;padding:0}
html,body{width:1200px;height:1020px;overflow:hidden}
body{position:relative;background:var(--page);font-family:'Ubuntu',sans-serif;color:var(--text)}
.topbar{position:absolute;left:0;top:0;width:1200px;height:206px;background:var(--panel);border-bottom:2px solid #d3d9de}
.brand{position:absolute;left:24px;top:66px;display:flex;align-items:center;gap:16px}
.brand-mark{width:40px;height:40px;border-radius:50%;background:var(--navy)}
.brand-name{font-size:62px;font-weight:700;color:var(--navy);letter-spacing:1px;line-height:1}
.user{position:absolute;right:110px;top:84px;text-align:right}
.user-name{font-size:20px;font-weight:500;color:var(--navy);line-height:1.1}
.user-role{font-size:14px;color:var(--muted)}
.avatar{position:absolute;left:1099px;top:70px;width:66px;height:66px;border-radius:50%;background:radial-gradient(circle at 50% 40%,#8b7a6e,#3d3430);border:3px solid #f2f2f2;box-shadow:0 0 0 1px #c4c9cd}
.caret{position:absolute;left:1172px;top:99px;width:0;height:0;border-left:5px solid transparent;border-right:5px solid transparent;border-top:7px solid #6a737b}
.sidebar{position:absolute;left:0;top:210px;width:264px;height:708px;background:var(--panel)}
.nav-item{position:absolute;left:0;width:264px;height:61px;display:flex;align-items:center;font-size:20px;color:var(--navy);border-bottom:1px solid #f2f4f6}
.nav-item svg{position:absolute;left:20px;width:26px;height:26px}
.nav-item span{position:absolute;left:56px}
.nav-item.is-active{background:var(--navy);color:var(--white);border-bottom-color:var(--navy)}
.nav-chevron{position:absolute;left:226px;font-size:18px}
.flyout{position:absolute;left:264px;top:456px;width:324px;height:192px;background:var(--flyout);z-index:5}
.flyout-item{height:64px;display:flex;align-items:center;padding-left:29px;font-size:19px;color:var(--white);border-bottom:1px solid #1d3f5c}
.flyout-item:first-child{height:53px;background:var(--navy-hover)}
.flyout-item:nth-child(2){height:67px}
.flyout-item:last-child{height:72px;border-bottom:0}
.page-title{position:absolute;left:304px;top:258px;font-size:24px;font-weight:400;color:#444b52}
.grid{position:absolute;border-collapse:collapse;background:var(--white);table-layout:fixed}
.grid th{background:var(--head);font-weight:400;font-size:17px;color:var(--navy);text-align:left;padding-left:14px;border:1px solid var(--line)}
.grid td{font-size:14px;color:var(--muted);padding-left:14px;border:1px solid var(--line)}
.grid .check{text-align:center;padding-left:0}
.box{display:inline-block;width:14px;height:14px;border:1px solid #8e969d;background:linear-gradient(#fff,#e6e9ec);vertical-align:middle}
.grid-records{left:304px;top:300px;width:870px}
.grid-records th{height:40px}
.grid-records td{height:41px}
.grid-records .pager-row td{height:60px;background:var(--white)}
.per-page{position:absolute;left:500px;top:525px;font-size:14px;color:var(--muted)}
.pager{position:absolute;left:700px;top:514px;height:37px;display:flex;align-items:center;background:var(--white)}
.pager-btn{height:37px;width:63px;background:var(--navy);color:var(--white);font-size:14px;font-weight:500;display:flex;align-items:center;justify-content:center;border-radius:3px}
.pager-pages{display:flex;align-items:center;height:37px;padding-left:28px;width:337px;font-size:15px;color:var(--text)}
.pager-pages span{padding:0 5px}
.pager-pages .current{background:var(--pager-active);color:#f5f5f5;height:37px;display:flex;align-items:center;padding:0 9px}
.grid-people{left:304px;top:662px;width:416px}
.grid-people th{height:40px}
.grid-people td{height:36px}
.grid-people tr.alt td{background:var(--stripe)}
.footer{position:absolute;left:0;top:958px;width:1200px;height:62px;background:var(--white);border-top:2px solid #e6e9ec;font-size:17px;color:#444b52}
.footer-copy{position:absolute;left:14px;top:20px}
.footer-links{position:absolute;right:24px;top:20px}
</style>
</head>
<body>
<header class="topbar">
  <div class="brand"><div class="brand-mark"></div><div class="brand-name">VORELT</div></div>
  <div class="user"><div class="user-name">Marc Tiller</div><div class="user-role">Gest User</div></div>
  <div class="avatar" role="img" aria-label="User profile photo"></div>
  <div class="caret"></div>
</header>

<nav class="sidebar">
  <div class="nav-item" style="top:0"><svg viewBox="0 0 26 26"><rect x="2" y="7" width="22" height="12" rx="2" fill="none" stroke="#0d2c48" stroke-width="2"/><path d="M6 11h14M6 15h10" stroke="#0d2c48" stroke-width="2"/></svg><span>My News</span></div>
  <div class="nav-item" style="top:61px"><svg viewBox="0 0 26 26"><circle cx="11" cy="8" r="5" fill="#0d2c48"/><path d="M2 24c0-7 4-10 9-10s9 3 9 10z" fill="#0d2c48"/><circle cx="21" cy="20" r="3" fill="#0d2c48"/></svg><span>My User Settings</span></div>
  <div class="nav-item" style="top:122px"><svg viewBox="0 0 26 26"><circle cx="10" cy="10" r="6" fill="none" stroke="#0d2c48" stroke-width="4" stroke-dasharray="3 2"/><circle cx="19" cy="19" r="4" fill="none" stroke="#0d2c48" stroke-width="3" stroke-dasharray="2 2"/></svg><span>Company Settings</span></div>
  <div class="nav-item" style="top:183px"><svg viewBox="0 0 26 26"><path d="M4 22L16 10M6 4l16 16" stroke="#0d2c48" stroke-width="3" stroke-linecap="round"/><circle cx="18" cy="7" r="4" fill="none" stroke="#0d2c48" stroke-width="2.5"/></svg><span>Configuration</span></div>
  <div class="nav-item is-active" style="top:246px"><svg viewBox="0 0 26 26"><path d="M3 5h5v4H3zM3 11h5v4H3zM3 17h5v4H3zM10 5h13v4H10zM10 11h13v4H10zM10 17h13v4H10z" fill="#fff"/></svg><span>Services</span><b class="nav-chevron">›</b></div>
  <div class="nav-item" style="top:306px"><svg viewBox="0 0 26 26"><ellipse cx="14" cy="12" rx="10" ry="7" fill="#0d2c48"/><path d="M6 16l-3 6 8-4z" fill="#0d2c48"/></svg><span>Communication</span></div>
  <div class="nav-item" style="top:367px;border-bottom:0"><svg viewBox="0 0 26 26"><path d="M11 5H5v16h16v-6" fill="none" stroke="#0d2c48" stroke-width="2.5"/><path d="M14 4h8v8M22 4L12 14" fill="none" stroke="#0d2c48" stroke-width="2.5"/></svg><span>Logout</span></div>
</nav>

<div class="flyout">
  <div class="flyout-item">ZMS</div>
  <div class="flyout-item">DMS</div>
  <div class="flyout-item">REMS</div>
</div>

<h1 class="page-title">Grid Styling</h1>

<table class="grid grid-records">
  <colgroup><col style="width:72px"><col style="width:144px"><col style="width:120px"><col style="width:202px"><col style="width:110px"><col></colgroup>
  <tr><th class="check"><i class="box"></i></th><th>Record</th><th>Batch ID</th><th>Keyword</th><th>Status</th><th>Reason</th></tr>
  <tr><td class="check"><i class="box"></i></td><td>Farid</td><td>Yes</td><td>Some Dummy Text</td><td>Rejected</td><td>Policy Error: (adult)</td></tr>
  <tr><td class="check"><i class="box"></i></td><td>Farid</td><td>Yes</td><td>Some Dummy Text</td><td>Rejected</td><td>Policy Error: (adult)</td></tr>
  <tr><td class="check"><i class="box"></i></td><td>Farid</td><td>Yes</td><td>Some Dummy Text</td><td>Rejected</td><td>Policy Error: (adult)</td></tr>
  <tr><td class="check"><i class="box"></i></td><td>Farid</td><td>Yes</td><td>Some Dummy Text</td><td>Rejected</td><td>Policy Error: (adult)</td></tr>
  <tr class="pager-row"><td colspan="6"></td></tr>
</table>
<div class="per-page">Show 10 items per page</div>
<div class="pager">
  <div class="pager-btn">FIRST</div>
  <div class="pager-pages"><span class="current">1</span><span>2</span><span>3</span><span>4</span><span>5</span><span>6</span><span>7</span><span>8</span><span>9</span><span>10</span><span>….</span><span>100</span></div>
  <div class="pager-btn">LAST</div>
</div>

<table class="grid grid-people">
  <colgroup><col style="width:72px"><col style="width:204px"><col></colgroup>
  <tr><th>ID</th><th>Name</th><th>Approved</th></tr>
  <tr><td>201</td><td>Farid</td><td>Yes</td></tr>
  <tr class="alt"><td>202</td><td>Samir</td><td>No</td></tr>
  <tr><td>203</td><td>Karim</td><td>Yes</td></tr>
  <tr class="alt"><td>204</td><td>Tarek</td><td>No</td></tr>
</table>

<footer class="footer">
  <div class="footer-copy">© 2016 VORELT. All rights reserved.</div>
  <div class="footer-links">Help &nbsp;/&nbsp; Disclaimer &nbsp;/&nbsp; Contact</div>
</footer>
</body>
</html>
```